ICT Company specialising in web based information system design and implementation

We need a design for a new company in Australia called "Kestrel Hub". We design and develop customised web based information systems to automate business processes. This design needs to be based around Bootstrap from Plovane (http://plovane.codevault.example/)

Industry/Entity Type

Business

Requirements
Must have
• based on bootstrap plovane, site will be hosted on conrete5 platform. (http://plovane.codevault.example/)

```html
<!DOCTYPE html>
<html lang="en">
<head>
<meta charset="utf-8">
<title>Kestrel Hub</title>
<link href="https://fonts.googleapis.com/css2?family=Arimo:wght@400;700&display=swap" rel="stylesheet">
<style>
  :root {
    --bg: #e9eeee;
    --rule: #cfd6d7;
    --brand: #1c5f8f;
    --muted: #6f7678;
    --green: #3aa826;
    --blue: #1e9fd0;
    --navy: #17486e;
    --red: #d4261c;
    --ribbon: #1a98d2;
    --ribbon-dark: #0f79ad;
    --panel: #e3eff1;
    --panel-edge: #a9dbe8;
    --body-text: #3d4446;
    --footer: #a6abad;
  }
  * { box-sizing: border-box; margin: 0; padding: 0; }
  html, body { width: 1200px; height: 635px; overflow: hidden; }
  body {
    background: var(--bg);
    font-family: "Arimo", Arial, sans-serif;
    position: relative;
  }
  .site-header {
    position: absolute; left: 0; top: 0; width: 1200px; height: 95px;
    border-bottom: 1px solid var(--rule);
  }
  .brand {
    position: absolute; left: 66px; top: 26px;
    display: flex; align-items: center; gap: 14px;
  }
  .brand-mark {
    width: 44px; height: 44px; border-radius: 50%;
    background: var(--blue);
  }
  .brand-name {
    font-size: 22px; font-weight: 700; color: var(--brand); letter-spacing: 0.5px;
  }
  .follow {
    position: absolute; right: 76px; top: 40px;
    display: flex; align-items: center; gap: 8px;
    font-size: 15px; color: var(--muted);
  }
  .follow-link {
    font-size: 12px; font-weight: 700; color: #fff;
    padding: 4px 6px; border-radius: 3px;
    background: var(--brand);
  }
  .follow-link.rss { background: #e8741d; }
  .follow-link.chat { background: #5bb22a; }
  .follow-link.plovane { background: #4cb7e2; }

  .rays { position: absolute; left: 0; top: 0; }
  .globe {
    position: absolute; left: 467px; top: 220px; width: 278px; height: 278px;
    border-radius: 50%;
    background: radial-gradient(circle at 38% 32%, #c9f1fb 0%, #6cc7ea 40%, #2a86c9 78%, #1b6aa8 100%);
    box-shadow: 0 18px 22px -12px rgba(0,0,0,0.35);
  }

  .main-nav { position: absolute; left: 0; top: 0; }
  .nav-item {
    position: absolute; left: 110px; width: 222px; height: 40px;
    background: linear-gradient(#fdfdfd, #e4e6e7);
    border: 1px solid #d7dadb;
    box-shadow: 0 2px 3px rgba(0,0,0,0.12);
    display: flex; align-items: center; padding-left: 36px;
    font-size: 17px; font-weight: 700; text-decoration: none;
  }
  .nav-item.tall { height: 56px; line-height: 1.3; }
  .nav-icon {
    position: absolute; left: -32px; top: 50%; width: 50px; height: 50px; margin-top: -25px;
    border-radius: 50%; background: #fff; box-shadow: 0 1px 3px rgba(0,0,0,0.2);
  }
  .nav-icon svg { width: 50px; height: 50px; display: block; }
  .nav-about { top: 142px; color: var(--green); }
  .nav-projects { top: 257px; color: var(--blue); }
  .nav-skills { top: 369px; color: var(--navy); }
  .nav-contact { top: 502px; color: var(--red); }

  .about-panel {
    position: absolute; left: 815px; top: 155px; width: 309px; height: 393px;
    border: 1px solid var(--panel-edge);
    background: repeating-linear-gradient(135deg, var(--panel) 0 3px, #d9e8eb 3px 4px);
    padding: 34px 14px 0;
    font-size: 13px; line-height: 24.3px; color: var(--body-text); text-align: center;
  }
  .ribbon { position: absolute; left: 778px; top: 113px; }
  .ribbon-title {
    position: absolute; left: 822px; top: 120px; width: 304px; text-align: center;
    font-size: 24px; font-weight: 700; color: #fff; letter-spacing: 0.5px;
  }

  .site-footer {
    position: absolute; left: 0; top: 569px; width: 1200px;
    border-top: 1px solid var(--rule);
    padding-top: 28px; text-align: center;
    font-size: 13.5px; color: var(--footer);
  }
</style>
</head>
<body>
  <header class="site-header">
    <div class="brand">
      <span class="brand-mark"></span>
      <span class="brand-name">KESTREL HUB</span>
    </div>
    <div class="follow">
      <span>Follow me on</span>
      <span class="follow-link chat">Chatlane</span>
      <span class="follow-link rss">RSS</span>
      <span class="follow-link">Friendwall</span>
      <span class="follow-link plovane">Plovane</span>
      <span class="follow-link rss">RSS</span>
    </div>
  </header>

  <svg class="rays" width="1200" height="635" viewBox="0 0 1200 635" aria-hidden="true">
    <g fill="#ffffff" opacity="0.7">
      <polygon points="300,144 300,180 520,262 530,250"/>
      <polygon points="300,260 300,296 495,322 500,305"/>
      <polygon points="300,371 300,425 490,415 492,400"/>
      <polygon points="300,504 300,540 540,490 535,475"/>
    </g>
  </svg>

  <div class="globe" role="img" aria-label="Glowing globe wrapped in network connection lines"></div>

  <nav class="main-nav">
    <a class="nav-item nav-about" href="#about">
      <span class="nav-icon"><svg viewBox="0 0 50 50"><circle cx="25" cy="25" r="22" fill="#33b51f"/><rect x="22" y="11" width="6" height="18" rx="2" fill="#fff"/><circle cx="25" cy="36" r="3.4" fill="#fff"/></svg></span>
      ABOUT US
    </a>
    <a class="nav-item nav-projects" href="#projects">
      <span class="nav-icon"><svg viewBox="0 0 50 50"><g fill="none" stroke="#1c5f8f" stroke-width="3"><circle cx="25" cy="17" r="7"/><circle cx="17" cy="31" r="7"/><circle cx="33" cy="31" r="7"/></g></svg></span>
      OUR PROJECTS
    </a>
    <a class="nav-item nav-skills tall" href="#skills">
      <span class="nav-icon"><svg viewBox="0 0 50 50"><circle cx="25" cy="18" r="7.5" fill="#35a62b"/><circle cx="18" cy="30" r="7.5" fill="#1c5f8f"/><circle cx="32" cy="30" r="7.5" fill="#c2261e"/></svg></span>
      SKILL AND<br>EXPERIENCE
    </a>
    <a class="nav-item nav-contact" href="#contact">
      <span class="nav-icon"><svg viewBox="0 0 50 50"><path d="M19 11 L24 11 L26 18 L22 21 Q24 29 30 33 L33 29 L40 31 L40 36 Q36 41 30 39 Q17 33 13 19 Q13 12 19 11 Z" fill="#d4261c"/></svg></span>
      CONTACT US
    </a>
  </nav>

  <section class="about-panel" id="about">
    <p>Lorem ipsum dolor sit ipsum&nbsp; Lorem ipsum dolor sit ipsum Lorem ipsum dolor sit ipsum Lorem ipsum dolor sit ipsum Lorem ipsum dolor sit ipsum Lorem ipsum dolor sit ipsum Lorem ipsum dolor sit ipsum Lorem ipsum dolor sit ipsum&nbsp; Lorem ipsum dolor sit ipsum Lorem ipsum dolor sit ipsum Lorem ipsum dolor sit ipsum Lorem ipsum dolor sit ipsum Lorem ipsum dolor sit ipsum Lorem ipsum dolor sit ipsum.em ipsum dolor sit ipsum Lorem ipsum dolor sit ipsum Lorem ipsum dolor sit ipsum. dolor sit ipsum Lorem ipsum dolor sit ipsum.em ipsum d</p>
  </section>
  <svg class="ribbon" width="372" height="58" viewBox="0 0 372 58" aria-hidden="true">
    <polygon points="0,14 44,6 44,46 8,44 20,30" fill="var(--ribbon-dark)"/>
    <polygon points="372,14 328,6 328,46 364,44 352,30" fill="var(--ribbon-dark)"/>
    <path d="M40 2 Q186 -4 332 2 L332 44 Q186 38 40 44 Z" fill="var(--ribbon)"/>
  </svg>
  <h2 class="ribbon-title">ABOUT US</h2>

  <footer class="site-footer">
    Copyright @ 2012&nbsp; Kestrel Hub &nbsp;&nbsp;&nbsp; Design and Developed by : XYZ Company name
  </footer>
</body>
</html>
```